New business card design

I need original, modern, business looking but dzen (minimalistic) looking design.
Also refer to websit trevanix.ru

Text is

Дробышев Кирилл, PMP
Партнер

Моб. +7 (915) 460 7185
info@trevanix.ru
Москва, Россия, 117342, ул. Береговая 7/2
=====================

Drobyshev Kirill, PMP
Partner

Mob. +7 (915) 460 7185
info@trevanix.ru
Moscow, Russia,117342, Beregovaya 7/2

Industry/Entity Type

Business

Font styles to use
Serif
Sans Serif

```html
<!DOCTYPE html>
<html lang="ru">
<head>
<meta charset="utf-8">
<title>Trevanix — business cards</title>
<link href="https://fonts.googleapis.com/css2?family=Didact+Gothic&display=swap" rel="stylesheet">
<style>
  :root {
    --backdrop: #d9d9d9;
    --card: #ffffff;
    --ink: #1f1f1f;
    --accent: #1a7fc8;
    --brand: #2a8fd4;
    --rule: #2a2a2a;
  }
  * { margin: 0; padding: 0; box-sizing: border-box; }
  html, body { width: 1200px; height: 500px; overflow: hidden; }
  body {
    background: var(--backdrop);
    font-family: "Didact Gothic", "Century Gothic", sans-serif;
    color: var(--ink);
    position: relative;
  }
  .card {
    position: absolute;
    top: 127px;
    width: 450px;
    height: 258px;
    background: var(--card);
  }
  .card--en { left: 97px; }
  .card--ru { left: 662px; }

  .brand {
    position: absolute;
    left: 24px;
    top: 110px;
    display: flex;
    align-items: center;
    gap: 10px;
  }
  .brand__mark {
    width: 34px;
    height: 34px;
    background: var(--brand);
  }
  .brand__name {
    font-size: 27px;
    color: var(--brand);
    letter-spacing: -0.3px;
  }

  .divider {
    position: absolute;
    left: 224px;
    top: 54px;
    width: 2px;
    height: 150px;
    background: var(--rule);
  }

  .details {
    position: absolute;
    left: 247px;
    top: 66px;
  }
  .details__name {
    font-size: 14.5px;
    text-transform: uppercase;
    letter-spacing: 0.1px;
    line-height: 16px;
  }
  .details__role {
    font-size: 12.5px;
    color: var(--accent);
    text-transform: uppercase;
    line-height: 15px;
    margin-bottom: 19px;
  }
  .contact {
    display: flex;
    align-items: flex-start;
    gap: 8px;
    font-size: 12px;
    line-height: 15px;
    margin-bottom: 9px;
  }
  .contact__icon {
    flex: none;
    width: 14px;
    height: 14px;
    background: var(--accent);
    display: flex;
    align-items: center;
    justify-content: center;
  }
  .contact__icon svg { display: block; }
</style>
</head>
<body>

  <section class="card card--en" lang="en">
    <div class="brand">
      <span class="brand__mark"></span>
      <span class="brand__name">Trevanix</span>
    </div>
    <div class="divider"></div>
    <div class="details">
      <p class="details__name">Drobyshev Kirill, PMP</p>
      <p class="details__role">Partner</p>
      <div class="contact">
        <span class="contact__icon"><svg width="8" height="10" viewBox="0 0 8 10"><rect x="0.75" y="0.75" width="6.5" height="8.5" rx="1" fill="none" stroke="#fff" stroke-width="1.3"/></svg></span>
        <span>+7 (915) 460 7185</span>
      </div>
      <div class="contact">
        <span class="contact__icon"><svg width="10" height="10" viewBox="0 0 10 10"><circle cx="4" cy="4" r="2.8" fill="none" stroke="#fff" stroke-width="1.4"/><line x1="6" y1="6" x2="9" y2="9" stroke="#fff" stroke-width="1.6"/></svg></span>
        <span>info@trevanix.ru</span>
      </div>
      <div class="contact">
        <span class="contact__icon"><svg width="8" height="11" viewBox="0 0 8 11"><path d="M4 10.5 C1.5 7 0.5 5.5 0.5 4 A3.5 3.5 0 0 1 7.5 4 C7.5 5.5 6.5 7 4 10.5Z" fill="#fff"/><circle cx="4" cy="4" r="1.3" fill="#1a7fc8"/></svg></span>
        <span>Moscow, Russia<br>117342, Beregovaya 7/2</span>
      </div>
    </div>
  </section>

  <section class="card card--ru" lang="ru">
    <div class="brand">
      <span class="brand__mark"></span>
      <span class="brand__name">Trevanix</span>
    </div>
    <div class="divider"></div>
    <div class="details">
      <p class="details__name">Дробышев Кирилл, PMP</p>
      <p class="details__role">Партнер</p>
      <div class="contact">
        <span class="contact__icon"><svg width="8" height="10" viewBox="0 0 8 10"><rect x="0.75" y="0.75" width="6.5" height="8.5" rx="1" fill="none" stroke="#fff" stroke-width="1.3"/></svg></span>
        <span>+7 (915) 460 7185</span>
      </div>
      <div class="contact">
        <span class="contact__icon"><svg width="10" height="10" viewBox="0 0 10 10"><circle cx="4" cy="4" r="2.8" fill="none" stroke="#fff" stroke-width="1.4"/><line x1="6" y1="6" x2="9" y2="9" stroke="#fff" stroke-width="1.6"/></svg></span>
        <span>info@trevanix.ru</span>
      </div>
      <div class="contact">
        <span class="contact__icon"><svg width="8" height="11" viewBox="0 0 8 11"><path d="M4 10.5 C1.5 7 0.5 5.5 0.5 4 A3.5 3.5 0 0 1 7.5 4 C7.5 5.5 6.5 7 4 10.5Z" fill="#fff"/><circle cx="4" cy="4" r="1.3" fill="#1a7fc8"/></svg></span>
        <span>Москва, Россия<br>117342, ул. Береговая 7/2</span>
      </div>
    </div>
  </section>

</body>
</html>
```